Business Card Design Project

KV Strategy Partners is a management consulting business with C-suite (CEO/CFO etc) target clients. Logo selected is blue with simple/serious typefaces.

Target Market(s)

CEOs and CFOs of large corporates

Industry/Entity Type

Management Consulting

Font styles to use
Serif

Colors
3276b5

Requirements
Must have
• Tag line: Building successful collaborations (use different font)
Address: 457 Cedar Brook Lane #03-22 Singapore 519307
Telephone: +65 8372 6094
Email: kvlorne@mailbox47.com

```html
<!DOCTYPE html>
<html lang="en">
<head>
<meta charset="utf-8">
<title>KV Strategy Partners – Business Card</title>
<link rel="stylesheet" href="https://fonts.googleapis.com/css2?family=Libre+Baskerville:wght@400;700&family=Lora:wght@400;500;600&family=Montserrat:wght@300;400&display=swap">
<style>
  :root {
    --stage: #686b73;
    --card: #ffffff;
    --brand-blue: #1ea7e4;
    --brand-blue-soft: #49b8ea;
    --panel-grey: #e9eaec;
    --band-grey: #5b5c60;
    --teal: #3a7c99;
    --ink: #2c2d30;
    --ink-soft: #45474c;
    --sub-grey: #55575c;
    --white: #ffffff;
  }
  * { margin: 0; padding: 0; box-sizing: border-box; }
  html, body {
    width: 1200px;
    height: 1082px;
    overflow: hidden;
    background: var(--stage);
    font-family: "Lora", Georgia, serif;
  }
  .stage {
    width: 1200px;
    height: 1082px;
    display: flex;
    align-items: center;
    justify-content: center;
  }
  .business-card {
    position: relative;
    width: 1000px;
    height: 571px;
    background: var(--card);
    overflow: hidden;
    box-shadow: 0 18px 40px rgba(0, 0, 0, 0.28);
  }
  .card-shapes {
    position: absolute;
    inset: 0;
    width: 100%;
    height: 100%;
  }
  .band-top { fill: var(--brand-blue); }
  .band-top-overlay { fill: var(--brand-blue-soft); }
  .contact-panel { fill: var(--panel-grey); }
  .band-bottom { fill: var(--band-grey); }
  .corner-triangle { fill: var(--teal); }

  .holder {
    position: absolute;
    left: 340px;
    top: 56px;
    display: flex;
    align-items: center;
    gap: 18px;
    color: var(--ink);
  }
  .holder-name {
    font-size: 28px;
    font-weight: 500;
    letter-spacing: 1.5px;
  }
  .holder-divider {
    width: 2px;
    height: 30px;
    background: var(--ink);
  }
  .holder-title {
    font-size: 16px;
    font-weight: 400;
    letter-spacing: 2px;
  }

  .brand {
    position: absolute;
    left: 470px;
    top: 196px;
    font-family: "Libre Baskerville", Georgia, serif;
  }
  .brand-main {
    color: var(--brand-blue);
    font-size: 50px;
    font-weight: 400;
    line-height: 1;
  }
  .brand-sub {
    margin-top: 12px;
    margin-left: 120px;
    color: var(--sub-grey);
    font-size: 24px;
    letter-spacing: 13px;
  }
  .tagline {
    position: absolute;
    left: 470px;
    top: 350px;
    width: 420px;
    font-family: "Montserrat", Arial, sans-serif;
    font-weight: 300;
    font-size: 17px;
    letter-spacing: 1.5px;
    color: var(--ink-soft);
  }

  .contact-list {
    position: absolute;
    left: 40px;
    top: 192px;
    list-style: none;
    display: flex;
    flex-direction: column;
    gap: 14px;
    color: var(--ink-soft);
    font-size: 15px;
  }
  .contact-item {
    display: flex;
    align-items: center;
    gap: 12px;
  }
  .contact-icon {
    width: 18px;
    height: 18px;
    flex: none;
    fill: none;
    stroke: var(--ink);
    stroke-width: 1.8;
  }
  .contact-icon .solid { fill: var(--ink); stroke: none; }

  .address {
    position: absolute;
    right: 40px;
    bottom: 54px;
    color: var(--white);
    font-size: 21px;
    letter-spacing: 0.8px;
  }
</style>
</head>
<body>
<main class="stage">
  <article class="business-card">
    <svg class="card-shapes" viewBox="0 0 1000 571" aria-hidden="true">
      <rect class="contact-panel" x="0" y="150" width="310" height="300"/>
      <rect class="band-top" x="0" y="0" width="1000" height="150"/>
      <rect class="band-top-overlay" x="0" y="0" width="310" height="150" opacity="0.55"/>
      <rect class="band-bottom" x="0" y="430" width="1000" height="141"/>
      <polygon class="corner-triangle" points="0,460 0,571 400,430"/>
    </svg>

    <header class="holder">
      <span class="holder-name">DANIEL KOH</span>
      <span class="holder-divider"></span>
      <span class="holder-title">GENERAL MANAGER</span>
    </header>

    <div class="brand">
      <div class="brand-main">KV Strategy</div>
      <div class="brand-sub">Partners</div>
    </div>

    <p class="tagline">Building successful collaborations</p>

    <ul class="contact-list">
      <li class="contact-item">
        <svg class="contact-icon" viewBox="0 0 18 18" aria-hidden="true"><path d="M4 2 L7 5 L5.5 7 Q7.5 10.5 11 12.5 L13 11 L16 14 L14 16 Q6 15 2 4 Z"/></svg>
        <span>+65 8372 6094</span>
      </li>
      <li class="contact-item">
        <svg class="contact-icon" viewBox="0 0 18 18" aria-hidden="true"><rect x="4.5" y="1.5" width="9" height="15" rx="1.5"/><line x1="7.5" y1="13.5" x2="10.5" y2="13.5"/></svg>
        <span>+65 9126 3058</span>
      </li>
      <li class="contact-item">
        <svg class="contact-icon" viewBox="0 0 18 18" aria-hidden="true"><rect x="5" y="2" width="8" height="5"/><rect x="2" y="7" width="14" height="9"/><rect class="solid" x="5" y="10" width="8" height="3"/></svg>
        <span>+65 6218 4470</span>
      </li>
      <li class="contact-item">
        <svg class="contact-icon" viewBox="0 0 18 18" aria-hidden="true"><rect x="1.5" y="4" width="15" height="10"/><polyline points="1.5,4 9,10 16.5,4"/></svg>
        <span>kvlorne@mailbox47.com</span>
      </li>
      <li class="contact-item">
        <svg class="contact-icon" viewBox="0 0 18 18" aria-hidden="true"><circle cx="9" cy="9" r="7.5"/><ellipse cx="9" cy="9" rx="3.2" ry="7.5"/><line x1="1.5" y1="9" x2="16.5" y2="9"/></svg>
        <span>www.kvstrategy.sg</span>
      </li>
    </ul>

    <p class="address">457 Cedar Brook Lane #03-22 Singapore 519307</p>
  </article>
</main>
</body>
</html>
```